Brintell's Business Card

I need some designs for a new business card including the new logo attached. An old example of our business card is also attached to show all the data that should be included on the new design.
**I added some more examples someone had mocked up**

Contact Information for Business Card

Should include all info on other examples uploaded.

```html
<!DOCTYPE html>
<html lang="en">
<head>
<meta charset="UTF-8">
<title>Brintell's Business Card</title>
<link href="https://fonts.googleapis.com/css2?family=Poppins:wght@400;500;600;700&display=swap" rel="stylesheet">
<style>
  :root {
    --page-bg: #111214;
    --card-bg: #26272a;
    --card-edge: #e3202a;
    --brand-blue: #1673c9;
    --brand-red: #e3202a;
    --text-light: #e9e9ea;
    --rule: #4a4b4f;
    --emboss: #3a3b3f;
  }
  * { box-sizing: border-box; margin: 0; padding: 0; }
  html, body { width: 1200px; height: 820px; overflow: hidden; }
  body {
    background: var(--page-bg);
    font-family: 'Poppins', sans-serif;
    position: relative;
  }
  .card {
    position: absolute;
    top: 255px;
    width: 540px;
    height: 310px;
    background: var(--card-bg);
    border: 3px solid var(--card-edge);
    overflow: hidden;
  }
  .card-front { left: 40px; }
  .card-back { left: 620px; }

  /* front */
  .brand {
    position: absolute;
    top: 46px;
    left: 0;
    width: 100%;
    text-align: center;
  }
  .brand-row { display: inline-flex; align-items: center; gap: 12px; }
  .brand-dot {
    width: 30px; height: 30px; border-radius: 50%;
    background: var(--brand-blue);
  }
  .brand-name {
    font-weight: 700;
    font-size: 46px;
    line-height: 1;
    letter-spacing: 1px;
    color: var(--brand-blue);
  }
  .brand-tagline {
    margin-top: 6px;
    font-weight: 500;
    font-size: 10.5px;
    letter-spacing: 0.6px;
    color: var(--brand-red);
  }
  .front-rule {
    position: absolute;
    left: 34px; right: 34px; top: 172px;
    height: 1px; background: var(--rule);
  }
  .holder {
    position: absolute;
    left: 34px; top: 186px;
    width: 230px;
  }
  .holder-name {
    font-weight: 600;
    font-size: 21px;
    color: var(--brand-blue);
    padding-bottom: 8px;
    border-bottom: 1px solid var(--rule);
    margin-bottom: 10px;
  }
  .contact-line {
    display: flex; align-items: center; gap: 9px;
    font-size: 14px; color: var(--text-light);
    line-height: 1.55;
  }
  .contact-line svg { width: 15px; height: 15px; flex: none; }
  .credentials {
    position: absolute;
    right: 30px; top: 196px;
    text-align: right;
    font-weight: 600;
    font-size: 13.5px;
    line-height: 1.45;
  }
  .credentials .blue { color: var(--brand-blue); }
  .credentials .red { color: var(--brand-red); }

  /* back */
  .back-mark {
    position: absolute;
    left: 30px; top: 45px;
    width: 220px; height: 220px;
    border-radius: 50%;
    border: 14px solid var(--emboss);
    display: flex; align-items: center; justify-content: center;
  }
  .back-mark-name {
    font-weight: 700;
    font-size: 26px;
    color: var(--emboss);
  }
  .back-copy {
    position: absolute;
    left: 280px; top: 98px;
    width: 240px;
  }
  .back-pitch {
    font-weight: 600;
    font-size: 13px;
    line-height: 1.35;
    color: var(--brand-blue);
  }
  .back-rule {
    width: 72px; height: 1px;
    background: var(--text-light);
    margin: 12px 0 10px;
  }
  .back-area {
    font-weight: 600;
    font-size: 14px;
    line-height: 1.35;
    color: var(--brand-red);
  }
</style>
</head>
<body>
  <section class="card card-front">
    <div class="brand">
      <div class="brand-row">
        <span class="brand-dot"></span>
        <span class="brand-name">BRINTELL'S</span>
      </div>
      <div class="brand-tagline">AIR CONDITIONING &amp; HEATING SERVICE</div>
    </div>
    <div class="front-rule"></div>
    <div class="holder">
      <div class="holder-name">DEAN MARLOW</div>
      <div class="contact-line">
        <svg viewBox="0 0 24 24" aria-hidden="true"><path fill="#e3202a" d="M6.6 10.8a15.1 15.1 0 0 0 6.6 6.6l2.2-2.2a1 1 0 0 1 1-.25 11.4 11.4 0 0 0 3.6.57 1 1 0 0 1 1 1V20a1 1 0 0 1-1 1A17 17 0 0 1 3 4a1 1 0 0 1 1-1h3.5a1 1 0 0 1 1 1c0 1.25.2 2.45.57 3.57a1 1 0 0 1-.25 1z"/></svg>
        <span>555.014.2290</span>
      </div>
      <div class="contact-line">
        <svg viewBox="0 0 24 24" aria-hidden="true"><path fill="#e3202a" d="M2 5h20v14H2z"/><path fill="none" stroke="#26272a" stroke-width="1.6" d="M2 5l10 8 10-8"/></svg>
        <span>hvacbrintell@mailbox.com</span>
      </div>
    </div>
    <div class="credentials">
      <div class="blue">LICENSED &amp; INSURED</div>
      <div class="red">FAMILY OWNED &amp; OPERATED</div>
    </div>
  </section>

  <section class="card card-back">
    <div class="back-mark" role="img" aria-label="Large embossed brand mark">
      <span class="back-mark-name">BRINTELL'S</span>
    </div>
    <div class="back-copy">
      <p class="back-pitch">CALL TODAY FOR ALL YOUR<br>HVAC, REFRIGERATION &amp;<br>PLUMBING NEEDS</p>
      <div class="back-rule"></div>
      <p class="back-area">Serves Ashford<br>IA &amp; Surrounding Areas</p>
    </div>
  </section>
</body>
</html>
```